Webdesign für B2B-Unternehmen
Zielgruppe
Wir sind im B2B Geschäft tätig und sind ein Spin Off der Firma www.plimora.com
Aufgabenstellung
Es soll sehr Übersichtlich und nicht zu verspielt sein. Unsere Potenziellen Kunden sollen sehr einfach und schnell an Ihr Ziel kommen

```html
<!DOCTYPE html>
<html lang="en">
<head>
<meta charset="utf-8">
<title>Veltrano – IT-Solutions</title>
<link rel="stylesheet" href="https://fonts.googleapis.com/css2?family=Noto+Sans:wght@400;700&family=Roboto:wght@400;500;700&display=swap">
<style>
:root{
  --navy-deep:#0b2740;
  --navy:#0a3556;
  --navy-mid:#0b4468;
  --footer:#0c2a42;
  --accent:#1e6a94;
  --accent-border:#2c7fb2;
  --white:#ffffff;
  --text-soft:#dbe6ee;
}
*{margin:0;padding:0;box-sizing:border-box}
html,body{width:1200px;height:2319px;overflow:hidden}
body{position:relative;background:var(--navy-deep);color:var(--white);font-family:"Noto Sans",sans-serif}
.abs{position:absolute}
a{color:var(--white)}

/* Navigation */
.nav a{position:absolute;top:38px;font-size:15px;text-decoration:underline;text-underline-offset:3px}
.brand{position:absolute;font-family:"Noto Sans",sans-serif;font-weight:400;letter-spacing:4px;color:var(--white);text-transform:uppercase}
.nav .brand{left:550px;top:36px;width:100px;text-align:center;font-size:17px;text-decoration:none}
.nav .contact{left:956px;top:39px;width:87px;height:28px;border:1.5px solid var(--white);border-radius:6px;text-decoration:none;text-align:center;line-height:25px;font-size:15px}

/* Hero */
.hero-image{left:0;top:0;width:1200px;height:665px;
  background:
    radial-gradient(ellipse at 50% 85%,rgba(240,190,110,.35),transparent 55%),
    radial-gradient(ellipse at 85% 70%,rgba(120,170,230,.35),transparent 50%),
    linear-gradient(180deg,#0d2d52 0%,#173f72 35%,#2a4f80 60%,#3a4c6a 80%,#2b3552 100%)}
.hero-title{left:0;width:1200px;text-align:center;font-family:"Roboto",sans-serif;font-weight:500;font-size:68px;top:268px}
.hero-sub{left:0;width:1200px;text-align:center;font-size:30px;top:352px}

/* Services */
.services{left:0;top:665px;width:1200px;height:683px;background:linear-gradient(180deg,#0b2f50 0%,var(--navy-mid) 55%,#0a3a5c 100%)}
.section-title{font-family:"Roboto",sans-serif;font-weight:500;font-size:52px}
.services-title{left:167px;top:748px}
.services-sub{left:167px;top:810px;font-size:24px}
.card{position:absolute;border:1.5px solid var(--white);border-radius:4px;text-align:center}
.card h3{font-weight:400;font-size:20px;margin-top:22px}
.card p{font-size:10.5px;line-height:17px;margin:18px auto 0;width:185px}
.card .btn{position:absolute;left:50%;transform:translateX(-50%);width:87px;height:28px;border-radius:4px;background:var(--white);color:var(--navy);font-weight:700;font-size:16px;line-height:28px}
.card-side{top:970px;width:218px;height:218px}
.card-side .btn{top:170px}
.card-featured{left:472px;top:951px;width:254px;height:255px;border:2px solid var(--accent-border)}
.card-featured h3{font-size:21px;margin-top:26px}
.card-featured p{width:210px;font-size:11px;line-height:19px;margin-top:16px}
.card-featured .btn{top:207px;background:var(--accent);color:var(--white)}

/* Social rail */
.social-round{position:absolute;border-radius:50%;background:var(--white)}
.social-square{position:absolute;border-radius:10px;background:var(--white)}

/* Feature */
.feature-image{left:0;top:1347px;width:1200px;height:694px;
  background:
    radial-gradient(ellipse at 22% 60%,rgba(205,190,60,.85),transparent 38%),
    linear-gradient(90deg,#4a4a30 0%,#56532a 25%,#2f4a66 55%,#203c5c 80%,#1a3452 100%)}
.feature-text{right:168px;text-align:right}
.feature-title{top:1481px;font-size:54px}
.feature-sub{top:1543px;font-size:24px}
.feature-list{top:1616px;list-style:none;font-size:26px;line-height:38px}
.cta{position:absolute;top:1814px;height:47px;background:var(--accent);color:var(--white);font-size:23px;line-height:47px;text-align:center;border-radius:2px}

/* Footer */
.footer{left:0;top:2041px;width:1200px;height:278px;background:var(--footer)}
.footer-brand{left:115px;top:2100px;font-size:26px;letter-spacing:6px}
.copyright{left:139px;top:2174px;font-family:"Roboto",sans-serif;font-weight:500;font-size:11px}
.privacy{left:139px;top:2213px;font-family:"Roboto",sans-serif;font-weight:700;font-size:10.5px}
.footer-links{right:313px;top:2100px;text-align:right;list-style:none;font-family:"Roboto",sans-serif;font-weight:700;font-size:15px;line-height:31.5px}
.footer-links a{text-decoration:underline}
.divider{left:916px;top:2097px;width:2px;height:183px;background:var(--white)}
.contact-block{left:941px;font-size:15px;color:var(--text-soft)}
.contact-block.head{font-family:"Roboto",sans-serif;font-weight:700;color:var(--white)}
</style>
</head>
<body>

<div class="abs hero-image" role="img" aria-label="Night city skyline with glowing network lines"></div>

<nav class="nav">
  <a href="#" style="left:139px">Banking</a>
  <a href="#" style="left:288px">Digital Identity &amp; Security</a>
  <a href="#" class="brand">Veltrano</a>
  <a href="#" style="left:734px">IoT</a>
  <a href="#" style="left:842px">SIM</a>
  <a href="#" class="contact">Contact</a>
</nav>

<h1 class="abs hero-title">Lorem Ipsum</h1>
<p class="abs hero-sub">We are your partner for IT-Solutions!</p>

<section class="abs services"></section>
<h2 class="abs section-title services-title">Lorem Ipsum</h2>
<p class="abs services-sub">We are your partner for IT-Solutions!</p>

<div class="card card-side" style="left:169px">
  <h3>Lorem Ipsum</h3>
  <p>Lorem ipsum dolor sit amet, consectetur adipiscing elit, sed do eiusmod tempor incididunt ut labore et dolore magna aliqua. Quis ipsum suspendisse ultrices gravida.</p>
  <span class="btn">More</span>
</div>
<div class="card card-featured">
  <h3>Lorem Ipsum</h3>
  <p>Lorem ipsum dolor sit amet, consectetur adipiscing elit, sed do eiusmod tempor incididunt ut labore et dolore magna aliqua. Quis ipsum suspendisse ultrices gravida.<br>Risus commodo viverra maecenas.</p>
  <span class="btn">More</span>
</div>
<div class="card card-side" style="left:813px">
  <h3>Lorem Ipsum</h3>
  <p>Lorem ipsum dolor sit amet, consectetur adipiscing elit, sed do eiusmod tempor incididunt ut labore et dolore magna aliqua. Quis ipsum suspendisse ultrices gravida.</p>
  <span class="btn">More</span>
</div>

<div class="abs feature-image" role="img" aria-label="Woman in a yellow shirt using her phone on a train"></div>

<div class="social-rail">
  <span class="social-round" style="left:1125px;top:1189px;width:42px;height:42px" aria-label="Social link"></span>
  <span class="social-square" style="left:1104px;top:1264px;width:66px;height:46px" aria-label="Video link"></span>
  <span class="social-round" style="left:1125px;top:1343px;width:42px;height:42px" aria-label="Social link"></span>
</div>

<h2 class="abs section-title feature-text feature-title">Lorem Ipsum dolor sit</h2>
<p class="abs feature-text feature-sub">We are your partner for IT-Solutions!</p>
<ul class="abs feature-text feature-list">
  <li>Et dolore magna</li>
  <li>Suspendisse ultrices</li>
  <li>consectetur adipiscing</li>
  <li>Incidunt ut labore</li>
</ul>
<span class="cta" style="left:696px;width:159px">More info</span>
<span class="cta" style="left:889px;width:137px">Buy now</span>

<footer class="abs footer"></footer>
<span class="brand footer-brand">Veltrano</span>
<p class="abs copyright">© 2020 All Rights reserved, Veltrano GmbH</p>
<a href="#" class="abs privacy">Privacy Policy</a>
<span class="social-round" style="left:139px;top:2254px;width:24px;height:24px" aria-label="Social link"></span>
<span class="social-round" style="left:174px;top:2254px;width:24px;height:24px" aria-label="Social link"></span>
<span class="social-square" style="left:209px;top:2256px;width:29px;height:20px;border-radius:5px" aria-label="Video link"></span>

<ul class="abs footer-links">
  <li><a href="#">IoT</a></li>
  <li><a href="#">SIM</a></li>
  <li><a href="#">Banking</a></li>
  <li><a href="#">Digital Identity &amp; Security</a></li>
  <li><a href="#">About us</a></li>
</ul>
<div class="abs divider"></div>
<p class="abs contact-block head" style="top:2100px">Visit Us</p>
<p class="abs contact-block" style="top:2132px;line-height:15px">Lindenweg 14<br>Halvorstadt, 54021</p>
<p class="abs contact-block head" style="top:2194px">Or Call Us...</p>
<p class="abs contact-block" style="top:2226px">01549 30271856</p>

</body>
</html>
```